PBG Business Card
Pelloway Building Group
PBG Business Card -
Creative Brief
Professional
Milo Pelloway
2274 Fenwick Avenue Shreveport, LA 71101
mpelloway@PellowayBG.com
PellowayBG.com
Logo and contact info on front. Logo to take up most of front of card with contact info in smaller text.
Pelloway Building Group (Notes) I would like a light grey color on the back with a navy border

```html
<!DOCTYPE html>
<html lang="en">
<head>
<meta charset="UTF-8">
<title>PBG Business Card</title>
<link rel="stylesheet" href="https://fonts.googleapis.com/css2?family=Source+Sans+3:wght@400;600;700&display=swap">
<style>
  :root {
    --card-bg: #ffffff;
    --navy: #1f3d73;
    --text: #2f2f2f;
    --divider: #9a9a9a;
    --icon: #333333;
  }
  * { margin: 0; padding: 0; box-sizing: border-box; }
  html, body {
    width: 1200px;
    height: 778px;
    overflow: hidden;
    background: var(--card-bg);
    font-family: "Source Sans 3", "Myriad Pro", Arial, sans-serif;
  }
  .card {
    position: relative;
    width: 1200px;
    height: 778px;
    background: var(--card-bg);
  }
  .brand {
    position: absolute;
    left: 96px;
    top: 330px;
    width: 440px;
    display: flex;
    align-items: center;
    gap: 22px;
  }
  .brand-square {
    width: 64px;
    height: 64px;
    background: var(--navy);
    flex-shrink: 0;
  }
  .brand-name {
    font-size: 40px;
    font-weight: 600;
    line-height: 1.15;
    color: var(--navy);
  }
  .divider {
    position: absolute;
    left: 600px;
    top: 88px;
    width: 3px;
    height: 498px;
    background: linear-gradient(to bottom, transparent, var(--divider) 15%, var(--divider) 85%, transparent);
  }
  .contact {
    position: absolute;
    left: 672px;
    top: 180px;
    color: var(--text);
  }
  .contact-name {
    font-size: 46px;
    font-weight: 600;
    color: var(--navy);
    line-height: 1;
    margin-bottom: 44px;
  }
  .contact-address {
    font-size: 30px;
    line-height: 48px;
    margin-bottom: 26px;
  }
  .contact-list { list-style: none; }
  .contact-list li {
    display: flex;
    align-items: center;
    gap: 14px;
    font-size: 30px;
    line-height: 41px;
  }
  .contact-list svg {
    width: 22px;
    height: 22px;
    fill: var(--icon);
    flex-shrink: 0;
  }
</style>
</head>
<body>
  <main class="card">
    <section class="brand">
      <div class="brand-square" aria-hidden="true"></div>
      <p class="brand-name">Pelloway Building Group</p>
    </section>

    <div class="divider"></div>

    <section class="contact">
      <h1 class="contact-name">Milo Pelloway</h1>
      <p class="contact-address">2274 Fenwick Avenue<br>Shreveport, LA 71101</p>
      <ul class="contact-list">
        <li>
          <svg viewBox="0 0 24 24" aria-hidden="true"><path d="M6.6 10.8c1.4 2.8 3.8 5.1 6.6 6.6l2.2-2.2c.3-.3.7-.4 1-.2 1.1.4 2.300.6 3.6.6.6 0 1 .4 1 1V20c0 .6-.4 1-1 1C10.6 21 3 13.4 3 4c0-.6.4-1 1-1h3.5c.6 0 1 .4 1 1 0 1.3.2 2.5.6 3.6.1.3 0 .7-.2 1z"/></svg>
          <span>318-555-0143</span>
        </li>
        <li>
          <svg viewBox="0 0 24 24" aria-hidden="true"><path d="M8 1h8c1.1 0 2 .9 2 2v18c0 1.1-.9 2-2 2H8c-1.1 0-2-.9-2-2V3c0-1.1.9-2 2-2zm0 3v13h8V4H8zm4 15a1.3 1.3 0 100 2.6 1.3 1.3 0 000-2.6z"/></svg>
          <span>318-555-0174</span>
        </li>
        <li>
          <svg viewBox="0 0 24 24" aria-hidden="true"><path d="M6 2h10l2 2v5H6V2zm-3 8h18c.6 0 1 .4 1 1v9c0 .6-.4 1-1 1H3c-.6 0-1-.4-1-1v-9c0-.6.4-1 1-1zm3 3v2h2v-2H6zm4 0v2h2v-2h-2zm4 0v2h4v-2h-4zm-8 4v2h2v-2H6zm4 0v2h2v-2h-2z"/></svg>
          <span>318-555-0146</span>
        </li>
        <li>
          <svg viewBox="0 0 24 24" aria-hidden="true"><path d="M2 5h20v14H2V5zm2 2v.5l8 5.5 8-5.5V7H4zm0 2.9V17h16V9.9l-8 5.5-8-5.5z"/></svg>
          <span>mpelloway@PellowayBG.com</span>
        </li>
        <li>
          <svg viewBox="0 0 24 24" aria-hidden="true"><path d="M12 2a10 10 0 100 20 10 10 0 000-20zm6.9 9h-3c-.1-2.3-.6-4.4-1.4-5.9A8 8 0 0118.9 11zM12 4c.9 1 1.8 3.5 1.9 7h-3.8C10.2 7.5 11.1 5 12 4zM9.5 5.1C8.7 6.6 8.2 8.7 8.1 11h-3a8 8 0 014.4-5.9zM5.1 13h3c.1 2.3.6 4.4 1.4 5.9A8 8 0 015.1 13zm6.9 7c-.9-1-1.8-3.5-1.9-7h3.8c-.1 3.5-1 6-1.9 7zm2.5-1.1c.8-1.5 1.3-3.6 1.4-5.9h3a8 8 0 01-4.4 5.9z"/></svg>
          <span>www.PellowayBG.com</span>
        </li>
      </ul>
    </section>
  </main>
</body>
</html>
```